Mondeko Ltd

I have been recommended by my web builder to get a fully designed website from two different companies such as yourselves. I have 5 products initially and need a site with world wide appeal.

Target Market(s)

Care Home and Nail Bar Industry

Industry/Entity Type

Builder

Number of Pages Required

5+ page

Font styles to use
Sans Serif

Colors

Designer to choose colors to be used in the design.

Requirements
Must have
• Great Innovative Home Page
Nice to have
• I would like the background moving as in clouds rushing past. Similar to the way car lights are speeded up in night time ads. I have vel-tor quality shots of various cloud formations that I can send
Should not have
• Usual boring design

```html
<!DOCTYPE html>
<html lang="en">
<head>
<meta charset="utf-8">
<title>Mondeko – Nail Bar &amp; Care Home</title>
<link rel="stylesheet" href="https://fonts.googleapis.com/css2?family=Open+Sans:ital,wght@0,300;0,400;0,600;0,700;1,400&family=Playfair+Display:wght@400&display=swap">
<style>
:root{
  --page-bg:#f6ebe8;
  --white:#ffffff;
  --band:#f1f1f1;
  --blue:#1a86c8;
  --ink:#222222;
  --text:#555555;
  --muted:#888888;
  --orange:#f5a11c;
  --list-bg:#f8ecea;
  --list-line:#ffffff;
  --hero-a:#7f8a8c;
  --hero-b:#c7b1a4;
}
*{margin:0;padding:0;box-sizing:border-box}
html,body{width:1200px;height:2609px;overflow:hidden}
body{background:var(--page-bg);font-family:"Open Sans",Arial,sans-serif;color:var(--ink)}
h2,h3{font-weight:400}
.page{position:absolute;left:132px;top:0;width:939px;height:2609px;background:var(--white)}
.abs{position:absolute}

/* header */
.phone-btn{left:19px;top:45px;width:145px;height:38px;background:var(--blue);color:#fff;font-size:13px;display:flex;align-items:center;justify-content:center;gap:4px}
.logo{left:380px;top:44px;width:180px;height:52px;display:flex;align-items:center;justify-content:center;gap:8px}
.logo-dot{width:14px;height:14px;border-radius:50%;background:var(--blue)}
.logo-name{font-family:"Playfair Display",Georgia,serif;font-weight:400;font-size:30px;color:var(--blue)}
.hours{left:586px;top:52px;font-size:13px;color:var(--orange)}
.social{display:flex;gap:9px}
.social span{width:10px;height:10px;border-radius:50%;background:#333}
.header-social{left:785px;top:57px}
.cart{left:907px;top:54px}
.rule{left:19px;top:127px;width:898px;height:5px;border-top:2px solid #333;border-bottom:1px solid #333}
.nav{top:147px;left:0;width:939px;height:20px;font-size:14px;font-weight:600;color:#111}
.nav a{position:absolute;transform:translateX(-50%);text-decoration:none;color:inherit;white-space:nowrap}

/* hero */
.hero{left:19px;top:179px;width:898px;height:386px;background:linear-gradient(100deg,var(--hero-a) 0%,var(--hero-b) 45%,#b49d92 70%,#8e7f7a 100%)}
.hero-title{position:absolute;right:44px;top:82px;text-align:right;color:#fff;font-size:52px;font-weight:300;line-height:70px;white-space:nowrap}
.hero-btn{position:absolute;left:512px;top:245px;width:269px;height:63px;border:2px solid #7fd0e0;color:#bfe7ee;font-size:14px;letter-spacing:2px;display:flex;align-items:center;justify-content:center;white-space:nowrap}
.hero-arrow{position:absolute;top:180px;color:#fff;font-size:22px}

/* welcome & services */
.h2{font-family:"Playfair Display",Georgia,serif;font-weight:400;font-size:40px;color:var(--ink);line-height:48px}
.sub{font-size:24px;color:var(--blue);line-height:30px}
.welcome{left:23px;top:592px}
.about-copy{left:26px;top:688px;width:572px;font-family:"Playfair Display",Georgia,serif;font-size:14.5px;line-height:25px;color:var(--muted)}
.btn{background:var(--blue);color:#fff;font-size:13px;display:flex;align-items:center;justify-content:center}
.btn-find{left:19px;top:850px;width:139px;height:40px;letter-spacing:1px}
.services-head{left:635px;top:592px}
.service-list{left:633px;top:692px;width:278px;background:var(--list-bg);list-style:none}
.service-list li{height:37.5px;border-bottom:2px solid var(--list-line);display:flex;align-items:center;justify-content:space-between;padding:0 24px 0 19px;font-size:11px;color:#333}
.service-list li::after{content:">";color:var(--blue);font-size:12px}

/* posts */
.posts{left:0;top:930px;width:939px;height:562px;background:var(--band)}
.center-head{width:939px;text-align:center}
.post{position:absolute;top:115px;width:287px;text-align:center}
.post-img{width:287px;height:176px}
.post-date{display:inline-block;margin-top:33px;background:var(--blue);color:#fff;font-size:12px;width:94px;height:21px;line-height:21px}
.post-title{font-family:"Playfair Display",Georgia,serif;font-weight:400;font-size:21px;line-height:31px;margin-top:18px;color:#222}
.post-meta{margin-top:14px;font-size:12px;color:#333;display:flex;justify-content:center;align-items:center;gap:6px}
.more-posts{left:0;top:508px;width:939px;text-align:center;font-size:18px;font-weight:700;letter-spacing:2px;color:#222}

/* testimonials */
.testimonial{position:absolute;top:1610px;width:290px;text-align:center}
.avatar{width:90px;height:90px;border-radius:50%;margin:0 auto;background:radial-gradient(circle,#e7d3c2 0%,#b99a82 60%,#8d8f91 100%)}
.quote{margin-top:30px;font-size:13px;line-height:19px;color:#444}
.person{margin-top:12px;font-family:"Playfair Display",Georgia,serif;font-size:21px;color:var(--muted);word-spacing:6px}
.role{font-size:11px;font-style:italic;color:var(--blue);margin-top:2px}
.dots{left:0;top:1883px;width:939px;display:flex;justify-content:center;gap:12px}
.dots span{width:5px;height:5px;border-radius:50%;background:#f4dcc0}
.dots span.on{background:var(--orange)}

/* care home */
.care{left:0;top:1927px;width:939px;height:452px;background:var(--band)}
.care-title{left:26px;top:44px}
.care-copy{left:21px;top:182px;width:500px;font-size:18px;line-height:25px;color:#444}
.btn-learn{left:18px;top:369px;width:139px;height:40px;font-size:17px;font-weight:600}
.care-img{left:584px;top:45px;width:333px;height:362px;background:linear-gradient(135deg,#8fae5a 0%,#c8d7a0 40%,#7fb6d8 75%,#dfe7ee 100%)}

/* footer */
.footer-logo{left:380px;top:2418px;width:180px;height:50px;display:flex;align-items:center;justify-content:center;gap:8px}
.footer-logo .logo-name{color:#222;font-size:28px}
.footer-nav{top:2497px;font-size:12px;font-weight:600}
.footer-social{left:0;top:2531px;width:939px;justify-content:center}
.footer-social span{width:9px;height:9px}
.copyright{left:0;top:2555px;width:939px;text-align:center;font-size:12px;color:#222}
</style>
</head>
<body>
<div class="page">

  <header>
    <div class="abs phone-btn">
      <svg width="14" height="14" viewBox="0 0 24 24" aria-hidden="true"><path fill="#fff" d="M6.6 10.8a15 15 0 0 0 6.6 6.6l2.2-2.2a1 1 0 0 1 1-.25 11.4 11.4 0 0 0 3.6.57 1 1 0 0 1 1 1V20a1 1 0 0 1-1 1A17 17 0 0 1 3 4a1 1 0 0 1 1-1h3.5a1 1 0 0 1 1 1c0 1.25.2 2.450.57 3.57a1 1 0 0 1-.25 1z"/></svg>
      353-555-0142
    </div>
    <div class="abs logo"><span class="logo-dot"></span><span class="logo-name">Mondeko</span></div>
    <div class="abs hours">Open: Mn - Sn 8am - 10PM</div>
    <div class="abs social header-social" aria-label="Social links"><span></span><span></span><span></span><span></span><span></span></div>
    <svg class="abs cart" width="22" height="20" viewBox="0 0 22 20" aria-label="Cart">
      <path d="M1 2h4l2.5 10h10l2-7H6" fill="none" stroke="#333" stroke-width="2"/>
      <circle cx="9" cy="16" r="1.6" fill="#333"/><circle cx="16" cy="16" r="1.6" fill="#333"/>
      <circle cx="19" cy="13" r="3" fill="var(--blue)"/>
    </svg>
    <div class="abs rule"></div>
    <nav class="abs nav">
      <a style="left:188px">HOME</a><a style="left:296px">ABOUT US</a><a style="left:416px">SERVICES</a><a style="left:529px">GALLERY</a><a style="left:630px">BLOG</a><a style="left:734px">CONTACT</a>
    </nav>
  </header>

  <section class="abs hero" role="img" aria-label="Photo of hands with colourful painted nails holding a mug">
    <div class="hero-title">Lorem ipsum dolor<br>sit amet consec</div>
    <div class="hero-btn">MAKE AN APPOINTMENT</div>
    <div class="hero-arrow" style="left:14px">&#8249;</div>
    <div class="hero-arrow" style="right:14px">&#8250;</div>
  </section>

  <section>
    <div class="abs welcome"><h2 class="h2">Welcome!</h2><div class="sub">About us</div></div>
    <p class="abs about-copy">Our Nail Bar opened its doors, with a team of talented, passionate, caring, creative people dedicated to doing great nails and giving our clients amazing experiences. We are always looking for the best, most natural products we can find. When you walk into our doors, you will be greeted with a smile and taken care of by everyone on our team. Every moment of your visit should be enjoyable and relaxed.</p>
    <div class="abs btn btn-find">FIND OUT MORE</div>

    <div class="abs services-head"><h2 class="h2">Our Services</h2><div class="sub">Out offer</div></div>
    <ul class="abs service-list">
      <li>MANICURES</li><li>INTUITIVE SERVICES</li><li>PEDICURES</li><li>MASSAGES</li><li>NAILS</li>
    </ul>
  </section>

  <section class="abs posts">
    <div class="abs center-head" style="top:24px"><h2 class="h2">Latest Posts</h2><div class="sub" style="font-size:22px">Blog updates</div></div>

    <article class="post" style="left:19px">
      <div class="post-img" role="img" aria-label="Photo of hands with bright multicoloured manicure" style="background:linear-gradient(135deg,#f3c7b0,#e9437a 55%,#f6d4c0)"></div>
      <span class="post-date">MAR 3,17</span>
      <h3 class="post-title">Ultra Glam Gold Nail Polishes for Holiday.</h3>
      <div class="post-meta"><span>&#9679; 0</span><span style="color:var(--orange)">&#9829;</span><span>10</span></div>
    </article>
    <article class="post" style="left:327px">
      <div class="post-img" role="img" aria-label="Photo of feet with pedicure among white orchids" style="background:linear-gradient(135deg,#e8c9b4,#f3e4ea 55%,#c987b4)"></div>
      <span class="post-date">MAR 3,17</span>
      <h3 class="post-title">Ultra Glam Gold Nail Polishes for Holiday.</h3>
      <div class="post-meta"><span>&#9679; 0</span><span style="color:var(--orange)">&#9829;</span><span>10</span></div>
    </article>
    <article class="post" style="left:630px">
      <div class="post-img" role="img" aria-label="Photo of hands with red polka dot nails on red fabric" style="background:linear-gradient(135deg,#f0c6ae,#c81e2a 55%,#a8141e)"></div>
      <span class="post-date">MAR 3,17</span>
      <h3 class="post-title">Ultra Glam Gold Nail Polishes for Holiday.</h3>
      <div class="post-meta"><span>&#9679; 0</span><span style="color:var(--orange)">&#9829;</span><span>10</span></div>
    </article>

    <div class="abs more-posts">MORE POSTS
      <svg width="32" height="12" viewBox="0 0 32 12" aria-hidden="true" style="vertical-align:middle"><path d="M0 6h24" stroke="var(--blue)" stroke-width="3"/><path d="M22 0l10 6-10 6z" fill="var(--blue)"/></svg>
    </div>
  </section>

  <section>
    <h2 class="abs center-head h2" style="top:1522px">Testimonial</h2>
    <div class="testimonial" style="left:-10px">
      <div class="avatar" role="img" aria-label="Portrait of client"></div>
      <p class="quote">Lorem ipsum dolor sit amet consectetur adipisc ing elit Nulla sed augue consectetur mattis nisi sit amet consequat magna Proin vitae urna vulputate purus sodales fringilla</p>
      <div class="person">Liam Carver</div><div class="role">Lorem ipsum dolor</div>
    </div>
    <div class="testimonial" style="left:317px">
      <div class="avatar" role="img" aria-label="Portrait of client"></div>
      <p class="quote">Lorem ipsum dolor sit amet consectetur adipisc ing elit Nulla sed augue consectetur mattis nisi sit amet consequat magna Proin vitae urna vulputate purus sodales fringilla</p>
      <div class="person">Liam Carver</div><div class="role">Lorem ipsum dolor</div>
    </div>
    <div class="testimonial" style="left:649px">
      <div class="avatar" role="img" aria-label="Portrait of client"></div>
      <p class="quote">Lorem ipsum dolor sit amet consectetur adipisc ing elit Nulla sed augue consectetur mattis nisi sit amet consequat magna Proin vitae urna vulputate purus sodales fringilla</p>
      <div class="person">Liam Carver</div><div class="role">Lorem ipsum dolor</div>
    </div>
    <div class="abs dots"><span></span><span class="on"></span><span></span></div>
  </section>

  <section class="abs care">
    <h2 class="abs care-title h2">Our outher service<br>Care Home</h2>
    <p class="abs care-copy">Lorem ipsum dolor sit amet, consectetur adipiscing elit. Fusce et lacus sit amet eros consequat congue eget eget metus. Interdum et malesuada fames ac ante ipsum primis in faucibus. Nunc eu viverra ex. Donec aliquam mi maximus mi interdum, eget tristique lacus pulvinar.</p>
    <div class="abs btn btn-learn">Learn More</div>
    <div class="abs care-img" role="img" aria-label="Photo of a carer with an elderly man outdoors among trees"></div>
  </section>

  <footer>
    <div class="abs footer-logo"><span class="logo-dot" style="background:#222"></span><span class="logo-name">Mondeko</span></div>
    <nav class="abs nav footer-nav">
      <a style="left:224px">HOME</a><a style="left:319px">ABOUT US</a><a style="left:423px">SERVICES</a><a style="left:521px">GALLERY</a><a style="left:611px">BLOG</a><a style="left:701px">CONTACT</a>
    </nav>
    <div class="abs social footer-social" aria-label="Social links"><span></span><span></span><span></span><span></span><span></span></div>
    <div class="abs copyright">© 2016 All Rights Reserved</div>
  </footer>

</div>
</body>
</html>
```